The World Most Wanted Eyelahes

1. We need a web design for a new company based in California, USA
2. We are the manufacturer for 100% human hair eyelashes,
made in Indonesia.
3. We recently launched "Tapered Eyelashes" with human hair.
Currently, none of the people carried Tapered eyelash.
4. We would like to see designs that use the 4 different colors that match with my products as "Four Seasons" concepts.
5. We prefer to follow www.velkro.com style, like professional website.
6. Focus on products as a manufacturer, therefore, all wholesaler and retailer copy and paste to their marketing tools.
7. Need bilingual English and Spanish.
8. Easy to link with social media.

Target Market(s)

United States and Central/South America.

Industry/Entity Type

Hair

Number of Pages Required

5+ page

Requirements
Must have
• 1. Details of Products with image.
• 2. Hottest/Newest Items "Tapered in 100% Human Hair"
• 3. Store Page
Nice to have
• 1. My competitors is Morvine Eyelash. http://www.morvinelashes.com/
• Please follow the concepts of it.
• 2. www.Velkro.com: They have great products detail on the website.
• i would like to focus on "Tapered" for new styles of the eyelash.
• 3. I want to visitors can write down the "Reviews" in every single product.
• Please check the www.QELCosmetics.com.
Should not have
• It's not salon/Shop for the beauty.
• No need an appointment.
• We are the manufacturer of the eyelash.

```html
<!DOCTYPE html>
<html lang="en">
<head>
<meta charset="utf-8">
<title>Lashora — Handmade with premium hair</title>
<link href="https://fonts.googleapis.com/css2?family=Raleway:wght@300;400;500;700&family=Great+Vibes&display=swap" rel="stylesheet">
<style>
:root{
  --gold:#c4923d;
  --gold-dark:#a8772a;
  --gold-light:#d3a75a;
  --page-bg:#a87d38;
  --white:#ffffff;
  --card:#f4f4f4;
  --footer:#f8f8f8;
  --text:#555555;
  --text-dark:#333333;
  --bar:#222222;
  --bar-text:#cfcfcf;
}
*{margin:0;padding:0;box-sizing:border-box}
html,body{width:1200px;height:1181px;overflow:hidden}
body{
  font-family:'Raleway',sans-serif;color:var(--text);
  background:linear-gradient(135deg,#b58a44 0%,#9c6f2c 40%,#b88d47 70%,#a07330 100%);
  position:relative;
}
.page{position:absolute;left:152px;top:0;width:896px;height:1181px;background:var(--white)}
.abs{position:absolute}
.logo{left:11px;top:8px;font-size:66px;font-weight:300;color:var(--gold);letter-spacing:-1px;line-height:1}
.top-links{top:19px;right:14px;display:flex;gap:22px;font-size:12.5px;color:var(--text-dark)}
.top-links span{display:flex;align-items:center;gap:5px}
.search{left:546px;top:55px;width:242px;height:37px;border:1px solid #e3e3e3;background:#f7f7f7;border-radius:3px;font-size:12px;color:#aaa;padding:11px 17px}
.search svg{position:absolute;right:14px;top:10px}
.cart{left:810px;top:54px}
.cart-count{left:852px;top:60px;font-size:11px;color:var(--text-dark);line-height:1.3}
.cart-count b{color:var(--gold);font-size:14px}
.nav{left:9px;top:113px;width:878px;height:45px;background:linear-gradient(var(--gold-light),var(--gold-dark));display:flex;color:var(--white);font-size:13px}
.nav a{display:flex;align-items:center;justify-content:center;color:inherit;text-decoration:none;height:100%}
.nav .active{background:rgba(255,255,255,.14);border-radius:3px 3px 0 0}
.nav .sep{width:1px;background:rgba(255,255,255,.3);height:26px;align-self:center}
.hero{left:9px;top:158px;width:878px;height:475px;background:radial-gradient(circle at 70% 55%,#f0b54a 0%,#b76d1c 30%,#5a2a0b 75%,#2a1205 100%);overflow:hidden}
.hero-photo{left:0;top:0;width:480px;height:475px;background:linear-gradient(90deg,#6b3a12,#c98a3f 55%,rgba(160,90,30,0));}
.hero-pack{left:443px;top:246px;width:162px;height:193px;border-radius:14px;background:linear-gradient(160deg,#e8c28a,#9a6a35 60%,#d9d9d9)}
.script{font-family:'Great Vibes',cursive;color:var(--white);line-height:1}
.s1{left:421px;top:57px;font-size:56px}
.s2{left:421px;top:104px;font-size:80px}
.tag1{left:444px;top:177px;font-size:19.5px;font-weight:300;color:var(--white)}
.tag2{left:444px;top:203px;font-size:19.5px;font-weight:700;color:var(--white)}
.feat{left:545px;top:335px;color:var(--white)}
.feat h3{font-size:14.5px;font-weight:700;margin-bottom:9px}
.feat li{list-style:none;font-size:13.5px;font-weight:500;margin-bottom:9px;padding-left:18px;position:relative}
.feat li::before{content:"";position:absolute;left:0;top:4px;width:10px;height:10px;border-radius:50%;background:var(--white)}
.dots{left:28px;top:435px;display:flex;gap:7px}
.dots i{width:14px;height:14px;border-radius:50%;background:rgba(255,255,255,.85)}
.dots i.on{background:transparent;border:2px solid var(--white)}
.card{top:644px;width:214px;height:223px;background:var(--card);text-align:center}
.card h4{font-size:15px;font-weight:500;color:#666;margin-top:21px}
.card h4.hl{color:var(--gold);font-weight:700}
.card p{font-size:10px;color:#555;margin-top:4px}
.pack{position:absolute;left:50px;top:68px;width:114px;height:152px;border-radius:12px}
.footer{left:0;top:885px;width:896px;height:225px;background:var(--footer)}
.col{top:37px}
.col h5{font-size:15px;font-weight:500;color:#666;margin-bottom:8px}
.col a{display:block;font-size:10px;color:var(--text-dark);text-decoration:none;line-height:21.5px}
.email{left:674px;top:55px;width:209px;height:38px;background:var(--white);border:1px solid #e2e2e2;font-size:10.5px;color:#888;padding:13px 15px}
.subscribe{left:675px;top:103px;width:115px;height:29px;background:var(--gold);color:var(--white);font-size:12px;font-weight:700;display:flex;align-items:center;justify-content:center;gap:8px;border-radius:2px}
.bar{left:0;top:1110px;width:896px;height:71px;background:var(--bar);display:flex;align-items:center;padding-left:18px;gap:30px;font-size:12.5px;color:var(--bar-text)}
.social{left:760px;top:1134px;display:flex;gap:9px}
.social i{width:24px;height:24px;background:#3a3a3a;border-radius:2px}
.social i.on{background:#1e88d6}
</style>
</head>
<body>
<div class="page">
  <div class="abs logo">LASHORA</div>
  <div class="abs top-links">
    <span><svg width="12" height="11" viewBox="0 0 12 11"><path d="M6 11 1 6A3 3 0 0 1 6 1.5 3 3 0 0 1 11 6Z" fill="#c4923d"/></svg>WISHLIST</span>
    <span><svg width="12" height="12" viewBox="0 0 12 12"><circle cx="6" cy="6" r="4.5" fill="none" stroke="#c4923d" stroke-width="3" stroke-dasharray="2 1.5"/></svg>MY ACCOUNT</span>
    <span><svg width="11" height="12" viewBox="0 0 11 12"><circle cx="5.5" cy="3.5" r="3" fill="#c4923d"/><path d="M0 12a5.5 5 0 0 1 11 0Z" fill="#c4923d"/></svg>LOGIN</span>
  </div>
  <div class="abs search">SEARCH SITE
    <svg width="18" height="18" viewBox="0 0 18 18"><circle cx="7.5" cy="7.5" r="6" fill="none" stroke="#c4923d" stroke-width="1.5"/><path d="M12 12l5 5" stroke="#c4923d" stroke-width="1.5"/></svg>
  </div>
  <svg class="abs cart" width="34" height="37" viewBox="0 0 34 37"><path d="M10 8a7 7 0 0 1 14 0" fill="none" stroke="#c4923d" stroke-width="2"/><rect x="1" y="8" width="32" height="29" rx="2" fill="#d9a148"/><path d="M9 15a8 8 0 0 0 16 0" fill="none" stroke="#fff" stroke-width="2"/></svg>
  <div class="abs cart-count">ITEMS<br>( <b>0</b> )</div>

  <nav class="abs nav">
    <a style="width:191px">NEWEST ITEMS</a><span class="sep"></span>
    <a style="width:153px">STORE</a><span class="sep"></span>
    <a style="width:152px">BLOG</a>
    <a class="active" style="width:178px">ABOUT US</a>
    <a style="flex:1">CONTACT</a>
  </nav>

  <section class="abs hero" role="img" aria-label="Golden glitter backdrop with a model wearing premium lashes">
    <div class="abs hero-photo" role="img" aria-label="Portrait of a model with gold makeup and long lashes"></div>
    <div class="abs hero-pack" role="img" aria-label="Lashora lash package, sparkling edition"></div>
    <div class="abs script s1">Handmade with</div>
    <div class="abs script s2">premium hair</div>
    <div class="abs tag1">COMPORTABLE WITH NATURAL AND SOFT</div>
    <div class="abs tag2">YOU LOOK MORE PERFECT WITH LASHORA</div>
    <div class="abs feat">
      <h3>SPARKLING YOUR EYES</h3>
      <ul><li>Lorem ipsum dolor sit ampet</li><li>Ipsum dolor sit ampet</li><li>Dolor sit ampet</li></ul>
    </div>
    <div class="abs dots"><i></i><i></i><i class="on"></i><i></i></div>
  </section>

  <div class="abs card" style="left:9px"><h4>SPARKLING YOUR EYES</h4><p>Lorem ipsum dolor sit ampet</p>
    <div class="pack" role="img" aria-label="Lash package, gold edition" style="background:linear-gradient(160deg,#f0b860,#8a4f1e 60%,#dcdcdc)"></div></div>
  <div class="abs card" style="left:230px"><h4 class="hl">BLOSSOM YOUR EYES</h4><p>Lorem ipsum dolor sit ampet</p>
    <div class="pack" role="img" aria-label="Lash package, pink edition" style="background:linear-gradient(160deg,#f7c8d0,#e59aa8 60%,#e3e3e3)"></div></div>
  <div class="abs card" style="left:452px"><h4>FACINATING YOUR EYES</h4><p>Lorem ipsum dolor sit ampet</p>
    <div class="pack" role="img" aria-label="Lash package, magenta edition" style="background:linear-gradient(160deg,#c2407e,#5a1a4a 60%,#dcdcdc)"></div></div>
  <div class="abs card" style="left:673px"><h4>DAZZLING YOUR EYES</h4><p>Lorem ipsum dolor sit ampet</p>
    <div class="pack" role="img" aria-label="Lash package, icy blue edition" style="background:linear-gradient(160deg,#d8e8f2,#9dbbd0 60%,#e6e6e6)"></div></div>

  <footer class="abs footer">
    <div class="abs col" style="left:18px"><h5>ABOUT US</h5><a>About LASHORA</a><a>How We Innovate</a><a>Jobs</a><a>Where to Buy</a></div>
    <div class="abs col" style="left:238px"><h5>MEDIA</h5><a>Lorem ipsum</a><a>Dolor sit ampet</a><a>Lorem ipsum dolor</a><a>Dolor sit ampet</a><a>Lorem ipsum sit</a><a>Dolor sit ampet</a></div>
    <div class="abs col" style="left:458px"><h5>SUPPORT</h5><a>Lorem ipsum</a><a>Dolor sit ampet</a><a>Lorem ipsum Dolor</a><a>Dolor sit ampet</a></div>
    <div class="abs col" style="left:674px"><h5>NEWSLETTER</h5></div>
    <div class="abs email">EMAIL ADDRESS</div>
    <div class="abs subscribe">SUBSCRIBE <svg width="7" height="11" viewBox="0 0 7 11"><path d="M1 1l4.5 4.5L1 10" fill="none" stroke="#fff" stroke-width="1.6"/></svg></div>
  </footer>

  <div class="abs bar"><span>© 2015 Lashora LTD.</span><span>PRIVACY &amp; SECURITY</span><span>SITE MAP</span><span>TERMS &amp; CONDITIONS</span></div>
  <div class="abs social"><i></i><i class="on"></i><i></i><i></i></div>
</div>
</body>
</html>
```